Business Card + Stationery Design for a Craft Beer Bar

Mr. Tovell's is a taproom sport bar that contains in its menu beers from different places around the world. What we offer differently is the experience that you can get inside our location, ambient music with rock from the 80s to 90s, projection with the sports of the moment, board games and private events.

Target Market(s)

Young people, Mid and High Class

Industry/Entity Type

Business

Font styles to use
Serif
Sans Serif

Colors
fee18a

Requirements
Must have
• Name, Title, Contact Details, Website
Nice to have
• Mail Signature
Should not have
• n/a

```html
<!DOCTYPE html>
<html lang="en">
<head>
<meta charset="utf-8">
<title>Mr. Tovell's – Business Card</title>
<link rel="stylesheet" href="https://fonts.googleapis.com/css2?family=Arimo:wght@400;700&display=swap">
<style>
  :root {
    --backdrop: #3b322d;
    --card: #1f2124;
    --gold: #f3ba43;
    --white: #ffffff;
    --ink: #f2f2f2;
    --dark-text: #2a2a2a;
  }
  * { box-sizing: border-box; margin: 0; padding: 0; }
  html, body { width: 1200px; height: 780px; overflow: hidden; }
  body {
    background: var(--backdrop);
    position: relative;
    font-family: "Arimo", Arial, sans-serif;
  }
  .card {
    position: absolute;
    width: 560px;
    height: 320px;
    background: var(--card);
    border-radius: 18px;
    overflow: hidden;
    box-shadow: 0 10px 30px rgba(0,0,0,.35);
  }
  .card--front { left: 40px; top: 100px; }
  .card--back  { left: 600px; top: 360px; }

  .brand {
    position: absolute;
    display: flex;
    flex-direction: row;
    align-items: center;
    justify-content: center;
    gap: 12px;
  }
  .brand__square {
    width: 18px; height: 18px;
    background: var(--gold);
    flex: none;
  }
  .brand__name {
    font-family: "Arimo", Arial, sans-serif;
    font-weight: 700;
    font-size: 34px;
    color: var(--gold);
    line-height: 1;
    white-space: nowrap;
  }
  .card--front .brand { left: 0; right: 0; top: 142px; }
  .card--back .brand { left: 20px; width: 250px; top: 120px; }
  .card--back .brand__name { font-size: 26px; }
  .card--back .brand__square { width: 14px; height: 14px; }

  .divider {
    position: absolute;
    left: 285px; top: 70px;
    width: 1px; height: 150px;
    background: var(--gold);
  }
  .contact {
    position: absolute;
    left: 310px; top: 62px;
    color: var(--ink);
    font-size: 14px;
    line-height: 1.35;
  }
  .contact__name { font-size: 21px; font-weight: 700; color: var(--white); }
  .contact__title { color: var(--gold); font-size: 14px; margin-bottom: 14px; }
  .contact__address { margin-bottom: 8px; }
  .contact__line { display: flex; align-items: center; gap: 8px; }
  .contact__icon { width: 15px; height: 15px; flex: none; }

  .band { position: absolute; left: 0; bottom: 0; width: 560px; height: 90px; }
  .website {
    position: absolute;
    right: 24px; bottom: 10px;
    color: var(--dark-text);
    font-size: 14px;
  }
</style>
</head>
<body>

  <section class="card card--front">
    <div class="brand">
      <span class="brand__square"></span>
      <span class="brand__name">Mr. Tovell's</span>
    </div>
  </section>

  <section class="card card--back">
    <div class="brand">
      <span class="brand__square"></span>
      <span class="brand__name">Mr. Tovell's</span>
    </div>

    <span class="divider"></span>

    <div class="contact">
      <p class="contact__name">Daniel Reyes</p>
      <p class="contact__title">Owner</p>
      <p class="contact__address">PO BOX 456 Harbour Lane<br>7th street Geelong</p>
      <p class="contact__line">
        <svg class="contact__icon" viewBox="0 0 16 16" aria-hidden="true">
          <circle cx="8" cy="8" r="7.5" fill="var(--gold)"/>
          <rect x="5.5" y="3.5" width="5" height="9" rx="1" fill="none" stroke="var(--card)" stroke-width="1.2"/>
        </svg>
        (555) 318-2046
      </p>
      <p class="contact__line">
        <svg class="contact__icon" viewBox="0 0 16 16" aria-hidden="true">
          <circle cx="8" cy="8" r="7.5" fill="var(--gold)"/>
          <rect x="4" y="5" width="8" height="6" fill="none" stroke="var(--card)" stroke-width="1.2"/>
          <path d="M4 5 L8 8.5 L12 5" fill="none" stroke="var(--card)" stroke-width="1.2"/>
        </svg>
        hello@tovellstap.com
      </p>
    </div>

    <svg class="band" viewBox="0 0 560 90" aria-hidden="true">
      <polygon points="0,8 345,8 345,14 0,14" fill="var(--white)"/>
      <path d="M0,24 L370,24 Q380,24 384,34 L388,44 L560,44 L560,90 L0,90 Z" fill="var(--gold)"/>
    </svg>
    <span class="website">www.tovellstaproom.com</span>
  </section>

</body>
</html>
```